依頼詳細
PCとスマホデザインの両方納品をいただきますが、
まずはデザインイメージが確認しやすいPCページのみの提案をお願いします。
PCページはアートボード幅を1366px、コンテンツ幅を1000pxのもので作成してください。
スマホページは当選者に納品時にお願いしたいと思います。
スマホサイズは横幅750pxのサイズで作成してください。

レスポンシブウェブデザインを意識したデザインでお願いします。

デザインに関しては、添付してあるデザインレイアウト設計シートを基にお願いします。
参考サイトのURLはデザインレイアウト設計シートに記載してあります。
画像データについては、フリー素材から流用してイメージ画像に当て込んでください。

足りない場合は、一旦他のサイトの写真をサンプルとして入れてください。(サンプルなどの表記をお願いします)
また、購入が必要な写真などを利用した場合、価格とサイト名を教えてください。
ページ数
1ページ
希望イメージ
シンプル 複雑
単色 カラフル
暗い 明るい
日常 高級
遊び心 厳粛
未来的 伝統的
女性的 男性的
希望する色
緑系
納品ファイル
• イラストレーター形式 (.ai)
• フォトショップ形式 (.psd)
• PNG形式 (.png)
補足説明
上記のいずれか1つ(アウトラインありとなしの2つ)と高解像度JPGを納品お願いします。

```html
<!DOCTYPE html>
<html lang="ja">
<head>
<meta charset="utf-8">
<title>あおば環境</title>
<link rel="stylesheet" href="https://fonts.googleapis.com/css2?family=Noto+Sans+JP:wght@400;500;700&family=Noto+Serif+JP:wght@500&display=swap">
<style>
:root{
  --green:#6cb52d;
  --green-dark:#4f9a1a;
  --green-pale:#f1f8e8;
  --orange:#f08a24;
  --chat:#3fbf5a;
  --ink:#333;
  --muted:#777;
  --rule:#ddd;
  --bg:#fff;
}
*{box-sizing:border-box;margin:0;padding:0}
html,body{width:1200px;height:4832px;overflow:hidden}
body{font-family:"Noto Sans JP",sans-serif;color:var(--ink);background:var(--bg);position:relative;font-size:14px;line-height:1.7}
.wrap{position:absolute;left:160px;width:880px}
.brand{display:flex;align-items:center;gap:10px;font-weight:700;color:var(--green);font-size:30px;letter-spacing:.04em}
.brand-mark{width:34px;height:34px;border-radius:50%;background:var(--green)}
.btn{display:flex;align-items:center;justify-content:center;color:#fff;font-weight:700;border-radius:4px;white-space:nowrap}
.btn-orange{background:var(--orange)}
.btn-chat{background:var(--chat)}
.tel{display:flex;align-items:center;gap:8px;font-weight:700;font-size:30px;letter-spacing:.02em;white-space:nowrap}
.tel small{display:block;font-size:10px;font-weight:400;line-height:1.3;color:var(--muted)}
.photo{background:linear-gradient(135deg,#c9cfc4,#8d9587)}

/* header */
.site-header{position:absolute;top:0;left:0;width:1200px;height:112px}
.site-header .brand{position:absolute;left:160px;top:34px}
.site-header .tel{position:absolute;left:460px;top:34px;font-size:26px}
.site-header .btn{position:absolute;top:42px;width:160px;height:32px;font-size:12px}
.global-nav{position:absolute;top:112px;left:0;width:1200px;height:40px;background:var(--green)}
.global-nav ul{list-style:none;display:flex;position:absolute;left:160px;width:880px;height:40px}
.global-nav li{flex:1;color:#fff;font-size:14px;font-weight:500;display:flex;align-items:center;justify-content:center}

/* hero */
.hero-photo{position:absolute;left:0;top:152px;width:820px;height:530px;background:linear-gradient(160deg,#e7ecef,#9aa6a0 60%,#6b7b66)}
.hero-copy{position:absolute;left:860px;top:200px;writing-mode:vertical-rl;font-family:"Noto Serif JP",serif;font-size:48px;letter-spacing:.18em;line-height:1.45;height:440px}

/* promises */
.promises{top:775px;height:290px;border:3px solid var(--green);display:flex;align-items:center}
.promises-title{width:260px;padding-left:60px;font-size:22px;line-height:1.9;font-weight:500}
.promises-title em{font-style:normal;color:var(--green)}
.promises-grid{display:grid;grid-template-columns:repeat(3,170px);gap:22px 24px}
.promise{text-align:center}
.promise svg{width:44px;height:44px}
.promise h3{font-size:13px;margin-top:4px}
.promise p{font-size:10px;color:var(--muted);line-height:1.5}

/* consult */
.consult{top:1250px;height:340px}
.consult .photo{position:absolute;left:0;top:0;width:500px;height:340px;background:linear-gradient(150deg,#d8dcd6,#6f7a6c)}
.consult-body{position:absolute;left:548px;top:20px;width:330px}
.consult-body h2{color:var(--green);font-size:22px;margin-bottom:14px}
.consult-body p{font-size:12px;color:#555;margin-bottom:22px}
.consult-body .btn{width:300px;height:40px;margin-bottom:12px;font-size:13px}

.section-title{font-size:26px;color:var(--green);font-weight:700}

/* services */
.services-title{top:1660px}
.services-grid{top:1730px;display:grid;grid-template-columns:436px 436px;gap:10px 8px}
.service{display:flex;height:185px}
.service .photo{width:218px}
.service-label{flex:1;background:var(--green);color:#fff;font-size:19px;font-weight:700;display:flex;align-items:center;justify-content:center}
.service-brand{width:218px;display:flex;align-items:center;justify-content:center;color:var(--green);font-weight:700;font-size:22px;gap:8px;border:1px solid var(--rule)}
.service-brand i{width:22px;height:22px;background:var(--green);display:block}

/* works */
.works{top:2555px}
.works p.lead{font-size:13px;margin-top:18px;color:#555}
.works-list{display:flex;gap:25px;margin-top:24px}
.work{width:276px}
.work .photo{height:150px;position:relative}
.work .tag{position:absolute;left:0;top:0;background:var(--green);color:#fff;font-size:12px;padding:2px 12px}
.work p{font-size:11px;color:#555;padding:12px 14px;border:1px solid var(--rule);border-top:0;height:78px}
.more{position:absolute;right:0;width:120px;height:30px;border:1px solid var(--green);color:var(--green);font-size:11px;display:flex;align-items:center;justify-content:center;border-radius:3px}

/* banners */
.banner-band{position:absolute;left:0;top:3230px;width:1200px;height:230px;background:#eef1ec}
.banner-band .inner{position:absolute;left:160px;top:20px;display:flex;gap:20px}
.banner{width:430px;height:190px;position:relative;display:flex;align-items:center;justify-content:center}
.banner span{position:relative;background:var(--green);color:#fff;font-size:24px;font-weight:700;padding:6px 26px}

/* news */
.news{top:3530px;display:flex;height:170px}
.news-title{writing-mode:vertical-rl;color:var(--green);font-size:24px;font-weight:700;letter-spacing:.3em;border-right:1px solid var(--green);padding-right:40px;margin-left:60px}
.news ul{list-style:none;margin-left:50px;width:560px}
.news li{display:flex;gap:40px;font-size:13px;padding:7px 0;border-bottom:1px dotted var(--rule)}
.news time{color:var(--muted)}

/* contact */
.contact{top:3880px;height:410px;background:var(--green-pale);border:3px solid #cde6b4}
.contact h2{text-align:center;color:var(--green);font-size:26px;margin-top:50px}
.contact .left{position:absolute;left:80px;top:140px;width:360px}
.contact .left h3{font-size:20px;margin-bottom:16px}
.contact .left p{font-size:12px;color:#555}
.contact .right{position:absolute;left:460px;top:140px;width:340px}
.contact .btn{height:44px;margin-bottom:14px;font-size:13px}

/* footer */
.site-footer{position:absolute;left:0;top:4400px;width:1200px;height:432px;border-top:6px solid var(--green)}
.site-footer .brand{position:absolute;left:160px;top:60px;font-size:26px}
.address{position:absolute;left:160px;top:120px;font-size:12px;color:var(--green-dark);line-height:1.9}
.sitemap{position:absolute;left:600px;top:60px;display:flex;gap:50px;font-size:12px}
.sitemap ul{list-style:none}
.sitemap li{margin-bottom:4px}
.sitemap li::before{content:"";display:inline-block;width:8px;height:8px;background:var(--green);margin-right:8px}
.sitemap li.sub{padding-left:16px;color:#555}
.sitemap li.sub::before{width:5px;height:5px;background:#999}
.copyright{position:absolute;left:0;bottom:20px;width:1200px;text-align:center;font-size:10px;color:#888}
</style>
</head>
<body>

<header class="site-header">
  <div class="brand"><span class="brand-mark"></span>あおば環境</div>
  <div class="tel">
    <svg width="30" height="22" viewBox="0 0 30 22"><rect x="1" y="1" width="28" height="20" rx="3" fill="none" stroke="#333" stroke-width="2"/><path d="M8 7h14M8 11h14M8 15h10" stroke="#333" stroke-width="2"/></svg>
    <div>0120-456-789<small>受付時間 9:00〜18:00 土日祝も対応</small></div>
  </div>
  <a class="btn btn-orange" style="left:690px">無料お見積り・ご相談</a>
  <a class="btn btn-chat" style="left:860px">チャットで簡単ご相談</a>
</header>
<nav class="global-nav">
  <ul><li>ホーム</li><li>サービス一覧 ▾</li><li>よくある質問</li><li>作業実績</li><li>会社案内</li></ul>
</nav>

<div class="hero-photo" role="img" aria-label="作業服の社員がバキュームカーのホースで作業する写真"></div>
<h1 class="hero-copy">お客様の<br>お困りごとに<br>対応する</h1>

<section class="wrap promises">
  <h2 class="promises-title">安心して<br>ご利用いただける<br><em>6つのお約束</em></h2>
  <div class="promises-grid">
    <div class="promise"><svg viewBox="0 0 44 44"><path d="M22 36 8 22a8 8 0 0 1 14-10 8 8 0 0 1 14 10z" fill="var(--green)"/></svg><h3>充実のサポート</h3><p>小さなご依頼でも丁寧に<br>最後までお手伝いします</p></div>
    <div class="promise"><svg viewBox="0 0 44 44"><path d="M6 22 22 8l16 14v16H6z" fill="none" stroke="var(--green)" stroke-width="3"/><rect x="18" y="26" width="8" height="12" fill="var(--green)"/></svg><h3>自宅にいるだけでOK</h3><p>ご連絡いただければ<br>すべてお任せください</p></div>
    <div class="promise"><svg viewBox="0 0 44 44"><path d="M22 38 6 22a9 9 0 0 1 16-11 9 9 0 0 1 16 11z" fill="none" stroke="var(--green)" stroke-width="3"/></svg><h3>営業を忘れません</h3><p>無理な勧誘はいたしません<br>安心してご相談ください</p></div>
    <div class="promise"><svg viewBox="0 0 44 44"><circle cx="22" cy="22" r="15" fill="none" stroke="var(--green)" stroke-width="3"/><path d="M22 13v9l6 4" stroke="var(--green)" stroke-width="3" fill="none"/></svg><h3>迅速できめ細かな対応</h3><p>最短で当日のお伺いにも<br>対応しております</p></div>
    <div class="promise"><svg viewBox="0 0 44 44"><path d="M22 5 36 10v12c0 9-6 15-14 17C14 37 8 31 8 22V10z" fill="var(--green)"/><path d="m15 22 5 5 9-10" stroke="#fff" stroke-width="3" fill="none"/></svg><h3>安心保証サービス</h3><p>作業後の不具合にも<br>責任を持って対応します</p></div>
    <div class="promise"><svg viewBox="0 0 44 44"><circle cx="22" cy="16" r="7" fill="var(--green)"/><path d="M8 38c2-9 8-13 14-13s12 4 14 13z" fill="var(--green)"/></svg><h3>お客様のための見積</h3><p>明確な料金をご提示し<br>追加費用はかかりません</p></div>
  </div>
</section>

<section class="wrap consult">
  <div class="photo" role="img" aria-label="作業車の前に並ぶ社員の集合写真"></div>
  <div class="consult-body">
    <h2>お見積もりご相談無料</h2>
    <p>浄化槽のことや不用品回収、遺品整理のご相談など、お困りのことがございましたらお気軽にお問い合わせください。スタッフが丁寧にご対応いたします。</p>
    <a class="btn btn-orange">無料お見積り・ご相談</a>
    <a class="btn btn-chat">チャットで簡単ご相談</a>
    <div class="tel">
      <svg width="30" height="22" viewBox="0 0 30 22"><rect x="1" y="1" width="28" height="20" rx="3" fill="none" stroke="#333" stroke-width="2"/><path d="M8 7h14M8 11h14M8 15h10" stroke="#333" stroke-width="2"/></svg>
      <div>0120-456-789<small>受付時間 9:00〜18:00</small></div>
    </div>
  </div>
</section>

<h2 class="wrap section-title services-title">サービス紹介</h2>
<section class="wrap services-grid">
  <div class="service"><div class="photo" role="img" aria-label="浄化槽の点検作業の写真"></div><div class="service-label">浄化槽維持管理</div></div>
  <div class="service"><div class="photo" role="img" aria-label="遺品の整理作業の写真"></div><div class="service-label">遺品整理</div></div>
  <div class="service"><div class="photo" role="img" aria-label="段ボールが積まれた室内の写真"></div><div class="service-label">丸ごとお片づけ</div></div>
  <div class="service"><div class="photo" role="img" aria-label="不用品を運び出すスタッフの写真"></div><div class="service-label">不用品回収</div></div>
  <div class="service"><div class="photo" role="img" aria-label="積み上げられた廃棄物の写真"></div><div class="service-label">廃棄物処理</div></div>
  <div class="service"><div class="service-brand"><i></i>住まいるあおば</div><div class="service-label">住まいるあおば</div></div>
  <div class="service"><div class="photo" style="background:linear-gradient(135deg,#f3dcd8,#d8b0a6)" role="img" aria-label="困りごとを相談する人の手元の写真"></div><div class="service-label">その他お困りごと</div></div>
</section>

<section class="wrap works">
  <h2 class="section-title">作業実績</h2>
  <p class="lead">年間作業実績2,400件!<br>あおば環境では、年間2,400件の作業実績がございます。<br>不用品回収はもちろん、不用品買取・遺品整理・生前整理など、お家のあらゆるお困りごとを解決いたします。</p>
  <div class="works-list">
    <div class="work"><div class="photo" role="img" aria-label="回収作業前後の部屋の写真"><span class="tag">不用品回収</span></div><p>部屋に放置していた不用品を短時間ですっきり回収いたしました。</p></div>
    <div class="work"><div class="photo" role="img" aria-label="片付け後の室内の写真"><span class="tag">丸ごとお片づけ</span></div><p>一軒家の丸ごとお片づけと不用品回収を行いました。</p></div>
    <div class="work"><div class="photo" role="img" aria-label="家具が並んだ倉庫の写真"><span class="tag">不用品回収</span></div><p>倉庫に眠っていた家具や家電を一括で回収いたしました。</p></div>
  </div>
  <a class="more" style="top:470px">作業一覧を見る ›</a>
</section>

<div class="banner-band">
  <div class="inner">
    <div class="banner photo" role="img" aria-label="会社の建物外観の写真"><span>会社案内</span></div>
    <div class="banner photo" role="img" aria-label="働くスタッフの写真"><span>採用情報</span></div>
  </div>
</div>

<section class="wrap news">
  <h2 class="news-title">新着情報</h2>
  <ul>
    <li><time>2021.4.19</time>事前工事に取り組んでいます!</li>
    <li><time>2021.4.19</time>一人立ちデビュー</li>
    <li><time>2021.4.16</time>社内研修会</li>
    <li><time>2021.4.12</time>車検に詳しい社員</li>
  </ul>
  <a class="more" style="top:150px">新着情報一覧を見る ›</a>
</section>

<section class="wrap contact">
  <h2>お困りごとをお聞かせください</h2>
  <div class="left">
    <h3>お見積もりご相談無料</h3>
    <p>浄化槽のことや不用品回収・遺品整理のご相談など、お困りのことがございましたら、お気軽にお問い合わせください。</p>
  </div>
  <div class="right">
    <a class="btn btn-orange">無料お見積り・ご相談</a>
    <a class="btn btn-chat">チャットで簡単ご相談</a>
    <div class="tel">
      <svg width="30" height="22" viewBox="0 0 30 22"><rect x="1" y="1" width="28" height="20" rx="3" fill="none" stroke="#333" stroke-width="2"/><path d="M8 7h14M8 11h14M8 15h10" stroke="#333" stroke-width="2"/></svg>
      <div>0120-456-789<small>受付時間 9:00〜18:00</small></div>
    </div>
  </div>
</section>

<footer class="site-footer">
  <div class="brand"><span class="brand-mark"></span>あおば環境</div>
  <p class="address">〒000-1143<br>緑川県青葉市若葉町1丁目2番3号<br>フリーダイヤル：0120-456-789<br>TEL：0000-00-0000<br>FAX：0000-00-0001<br>E-mail：info@aoba-kankyo.example</p>
  <div class="sitemap">
    <ul><li>サービス一覧</li><li class="sub">浄化槽維持管理</li><li class="sub">丸ごとお片づけ</li><li class="sub">不用品回収</li><li class="sub">廃棄物処理</li><li class="sub">遺品整理</li><li class="sub">住まいるあおば</li><li class="sub">その他お困りごと</li></ul>
    <ul><li>よくある質問</li><li>作業実績</li><li>会社案内</li><li>採用情報</li></ul>
    <ul><li>無料お見積り</li><li>お問い合わせ</li></ul>
  </div>
  <p class="copyright">Copyright © あおば環境 All Rights Reserved.</p>
</footer>

</body>
</html>
```